Banner for home page on event planning site

We are revamping the home page www.harborlanecelebrations.com and would like to add a banner to the center of it to guide potential clients to one of 3 areas of the site:

Weddings, Corporate Events, Parties and More

I'm uploading an attachment that shows where the banner will be placed. It needs to have those 3 distinct sections, and match the existing colors/branding of the site. The fonts used for the logo are Lucida Bright and Callie Hand. Both are available for free.

Please use lorem ipsum under each section, I'll fill that in later. It should just be highly designed, beautiful, and easy to understand that clicking these will take you to the different areas of the site.
Updates

Hi designers,
Here are some problems we are having with the designs that have been submitted.
1) 3 stock images as squares... when you do this and then put it into the existing website, it gets lost among the other boxes. We need this to be where the eye goes immediately when you land on the site.
2) Not enough of a frame or white space... we think you need some white space to make this stand out as different from the surrounding area.
3) No clearly defined areas. It needs to be easy for people to figure out... Weddings, click here. Parties, click here. Corporate events, click here.

Industry/Entity Type

Event Planning

Requirements
Should not have
• Nothing with orchids, her competitor uses them and they are common in the event planning industry. We want to stay away from them.

```html
<!DOCTYPE html>
<html lang="en">
<head>
<meta charset="utf-8">
<title>Harbor Lane Celebrations – Event Areas Banner</title>
<link rel="stylesheet" href="https://fonts.googleapis.com/css2?family=Parisienne&family=Libre+Baskerville:ital,wght@1,400;1,700&family=Roboto:wght@700&display=swap">
<style>
  :root {
    --page-bg: #ffffff;
    --list-text: #ffffff;
    --button-text: #ffffff;

    --wedding-photo-a: #efece8;
    --wedding-photo-b: #d9d4cf;
    --wedding-photo-c: #a89c92;
    --wedding-ribbon-top: #f6f7a8;
    --wedding-ribbon-bottom: #e4e400;
    --wedding-ribbon-fold: #b8b800;
    --wedding-title: #737a3a;
    --wedding-button: #6b2a8c;

    --corporate-photo-a: #5a2a12;
    --corporate-photo-b: #9a4a1c;
    --corporate-photo-c: #c9772e;
    --corporate-ribbon-top: #f7c76a;
    --corporate-ribbon-bottom: #e08f14;
    --corporate-ribbon-fold: #a9650c;
    --corporate-title: #8a3e1e;
    --corporate-button: #c98516;

    --party-photo-a: #2a1606;
    --party-photo-b: #7a4a10;
    --party-photo-c: #e3a232;
    --party-ribbon-top: #f2f8d4;
    --party-ribbon-bottom: #d5e784;
    --party-ribbon-fold: #a6b94a;
    --party-title: #c0392b;
    --party-button: #b5bd1e;
  }

  * { box-sizing: border-box; margin: 0; padding: 0; }

  html, body {
    width: 1200px;
    height: 280px;
    overflow: hidden;
    background: var(--page-bg);
  }

  .event-banner {
    position: relative;
    width: 1200px;
    height: 280px;
  }

  .event-card {
    position: absolute;
    top: 11px;
    width: 385px;
    height: 260px;
    border-radius: 22px;
    overflow: hidden;
  }
  .event-card--weddings  { left: 11px; }
  .event-card--corporate { left: 407px; }
  .event-card--parties   { left: 806px; }

  .event-card__photo {
    position: absolute;
    inset: 0;
  }
  .event-card--weddings .event-card__photo {
    background: linear-gradient(110deg, var(--wedding-photo-c) 0%, var(--wedding-photo-a) 30%, var(--wedding-photo-b) 60%, var(--wedding-photo-a) 85%, var(--wedding-photo-c) 100%);
  }
  .event-card--corporate .event-card__photo {
    background: linear-gradient(90deg, var(--corporate-photo-a) 0%, var(--corporate-photo-b) 25%, var(--corporate-photo-c) 50%, var(--corporate-photo-b) 75%, var(--corporate-photo-a) 100%);
  }
  .event-card--parties .event-card__photo {
    background: radial-gradient(ellipse at 70% 60%, var(--party-photo-c) 0%, var(--party-photo-b) 45%, var(--party-photo-a) 100%);
  }

  .event-card__ribbon {
    position: absolute;
    left: 0;
    top: 0;
    width: 385px;
    height: 110px;
  }

  .event-card__title {
    position: absolute;
    top: 38px;
    height: 60px;
    font-family: "Parisienne", cursive;
    font-size: 40px;
    line-height: 60px;
    white-space: nowrap;
  }
  .event-card--weddings .event-card__title  { left: 34px; color: var(--wedding-title); }
  .event-card--corporate .event-card__title { left: 0; width: 385px; text-align: center; color: var(--corporate-title); font-size: 36px; }
  .event-card--parties .event-card__title   { left: 0; width: 385px; text-align: center; color: var(--party-title); }

  .event-card__list {
    position: absolute;
    left: 26px;
    top: 152px;
    list-style: none;
    font-family: "Libre Baskerville", serif;
    font-style: italic;
    font-size: 16px;
    line-height: 24.5px;
    color: var(--list-text);
    text-shadow: 0 1px 2px rgba(0, 0, 0, 0.35);
  }
  .event-card__list li.event-card__sub { padding-left: 8px; }

  .event-card__button {
    position: absolute;
    left: 200px;
    bottom: 0;
    width: 148px;
    height: 30px;
    border-radius: 14px 14px 0 0;
    font-family: "Roboto", sans-serif;
    font-weight: 700;
    font-size: 14.5px;
    line-height: 32px;
    text-align: center;
    color: var(--button-text);
    text-decoration: none;
  }
  .event-card--weddings .event-card__button  { left: 197px; background: var(--wedding-button); }
  .event-card--corporate .event-card__button { background: var(--corporate-button); }
  .event-card--parties .event-card__button   { left: 202px; background: var(--party-button); }
</style>
</head>
<body>
<main class="event-banner">

  <section class="event-card event-card--weddings">
    <div class="event-card__photo" role="img" aria-label="Close-up photo of the lace back of a white wedding dress"></div>
    <svg class="event-card__ribbon" viewBox="0 0 385 110" aria-hidden="true">
      <defs>
        <linearGradient id="wedding-ribbon" x1="0" y1="0" x2="0" y2="1">
          <stop offset="0" stop-color="var(--wedding-ribbon-top)"/>
          <stop offset="1" stop-color="var(--wedding-ribbon-bottom)"/>
        </linearGradient>
      </defs>
      <path d="M0,30 C0,18 6,12 16,12 L16,40 L0,44 Z" fill="var(--wedding-ribbon-fold)"/>
      <path d="M0,50 Q0,38 14,38 L320,38 Q372,40 385,78 L385,98 L18,98 Q0,98 0,84 Z" fill="url(#wedding-ribbon)"/>
    </svg>
    <h2 class="event-card__title">Weddings</h2>
    <ul class="event-card__list">
      <li>Lorem Ipsum</li>
      <li class="event-card__sub">- Lorem Ipsum</li>
      <li class="event-card__sub">- Lorem Ipsum</li>
      <li class="event-card__sub">- Lorem Ipsum</li>
    </ul>
    <a class="event-card__button" href="#weddings">More Info</a>
  </section>

  <section class="event-card event-card--corporate">
    <div class="event-card__photo" role="img" aria-label="Photo of a draped curtain backdrop with white branch and lantern decor"></div>
    <svg class="event-card__ribbon" viewBox="0 0 385 110" aria-hidden="true">
      <defs>
        <linearGradient id="corporate-ribbon" x1="0" y1="0" x2="0" y2="1">
          <stop offset="0" stop-color="var(--corporate-ribbon-top)"/>
          <stop offset="1" stop-color="var(--corporate-ribbon-bottom)"/>
        </linearGradient>
      </defs>
      <path d="M0,30 C0,18 6,12 16,12 L16,40 L0,44 Z" fill="var(--corporate-ribbon-fold)"/>
      <path d="M0,50 Q0,38 14,38 L320,38 Q372,40 385,78 L385,98 L18,98 Q0,98 0,84 Z" fill="url(#corporate-ribbon)"/>
    </svg>
    <h2 class="event-card__title">Corporate Events</h2>
    <ul class="event-card__list">
      <li>Lorem Ipsum</li>
      <li class="event-card__sub">- Lorem Ipsum</li>
      <li class="event-card__sub">- Lorem Ipsum</li>
      <li class="event-card__sub">- Lorem Ipsum</li>
    </ul>
    <a class="event-card__button" href="#corporate-events">More Info</a>
  </section>

  <section class="event-card event-card--parties">
    <div class="event-card__photo" role="img" aria-label="Photo of golden confetti falling under bright stage lights"></div>
    <svg class="event-card__ribbon" viewBox="0 0 385 110" aria-hidden="true">
      <defs>
        <linearGradient id="party-ribbon" x1="0" y1="0" x2="0" y2="1">
          <stop offset="0" stop-color="var(--party-ribbon-top)"/>
          <stop offset="1" stop-color="var(--party-ribbon-bottom)"/>
        </linearGradient>
      </defs>
      <path d="M0,30 C0,18 6,12 16,12 L16,40 L0,44 Z" fill="var(--party-ribbon-fold)"/>
      <path d="M0,50 Q0,38 14,38 L320,38 Q372,40 385,78 L385,98 L18,98 Q0,98 0,84 Z" fill="url(#party-ribbon)"/>
    </svg>
    <h2 class="event-card__title">Parties</h2>
    <ul class="event-card__list">
      <li>Lorem Ipsum</li>
      <li class="event-card__sub">- Lorem Ipsum</li>
      <li class="event-card__sub">- Lorem Ipsum</li>
      <li class="event-card__sub">- Lorem Ipsum</li>
    </ul>
    <a class="event-card__button" href="#parties">More Info</a>
  </section>

</main>
</body>
</html>
```